Ecommerce website Home Page Design that is clean and elegant

Design a Home page for an ecommerce website. This website products and offerings will be very similar to :

breezyharborcharms.com
maplecrestbazaar.com

Target Market(s)

Consumer and small shops who can order online.

Industry/Entity Type

Retail

Number of Pages Required

1 page

Colors

Designer to choose colors to be used in the design.

Requirements
Must have
• Exact competition with similar products:
• breezyharborcharms.com
• http://www.maplecrestbazaar.com/
• Home page with featured image banner
• List of items on sale or category based items list
• atleast three banners for sale or shipping related offers.
Nice to have
• The logo has very light colors and products will have lots of colors as you can see on competition sites. So the design must consider this so that logo also stands out somewhat for branding purpose.
Should not have
• Design should not have black background

```html
<!DOCTYPE html>
<html lang="en">
<head>
<meta charset="utf-8">
<title>Novabrite – Home</title>
<link href="https://fonts.googleapis.com/css2?family=Open+Sans:wght@300;400;600;700&family=Roboto+Slab:wght@300;400;700&display=swap" rel="stylesheet">
<style>
:root{
  --teal:#5ea7b1;
  --teal-dark:#4a8f99;
  --yellow:#eaae3c;
  --pink:#f5a0b3;
  --nav:#3b3b3b;
  --ink:#333;
  --muted:#777;
  --light:#f0f0f0;
  --white:#fff;
}
*{box-sizing:border-box;margin:0;padding:0}
html,body{width:1200px;height:3516px;overflow:hidden}
body{position:relative;background:var(--white);font-family:'Open Sans',sans-serif;color:var(--ink);line-height:1.3}
.abs{position:absolute}

/* top bar */
.topbar{left:0;top:0;width:1200px;height:42px;border-bottom:1px solid #e5e5e5;font-size:12px;color:#666}
.topbar .links{position:absolute;left:87px;top:13px;white-space:nowrap}
.topbar .links span{margin-right:6px}
.topbar .links .active{color:var(--teal)}
.topbar .login{position:absolute;left:980px;top:13px}
.topbar .cart{position:absolute;left:1052px;top:0;width:59px;height:42px;background:var(--teal);color:#fff;font-size:10px;text-align:center;padding-top:24px}
.cart::before{content:"";position:absolute;left:23px;top:7px;width:13px;height:11px;border:2px solid #fff;border-radius:0 0 3px 3px}

/* header */
.logo{left:87px;top:52px;font-family:'Roboto Slab',serif;font-weight:700;font-size:46px;line-height:56px;color:var(--teal);letter-spacing:-1px}
.search{left:492px;top:66px;width:380px;height:37px;border:1px solid #ddd;border-radius:3px;font-size:12px;color:#aaa;padding:10px 14px}
.search .btn{position:absolute;right:-1px;top:-1px;width:52px;height:37px;background:var(--yellow);border-radius:0 3px 3px 0}
.search .btn svg{position:absolute;left:18px;top:11px}
.call{left:914px;top:73px;font-size:16px;font-weight:700;color:var(--ink);white-space:nowrap}
.call b{color:var(--teal);font-weight:600}

/* nav */
.nav{left:0;top:131px;width:1200px;height:35px;background:var(--nav)}
.nav ul{position:absolute;left:89px;width:1024px;display:flex;list-style:none;height:35px;align-items:center;justify-content:space-between;color:#fff;font-size:14px}
.nav li{padding:0 14px;height:35px;line-height:35px}
.nav .home{background:var(--yellow)}
.nav .sale{background:var(--teal)}

/* hero */
.hero{left:0;top:166px;width:1200px;height:418px;background:linear-gradient(180deg,#9dc6d6 0%,#bcd6df 38%,#8fc2c6 48%,#e6ded0 70%,#efe6d8 100%)}
.hero .frame{position:absolute;left:148px;top:73px;width:2px;height:272px;background:#fff}
.hero .frame::before,.hero .frame::after{content:"";position:absolute;left:0;width:40px;height:2px;background:#fff}
.hero .frame::before{top:0}.hero .frame::after{bottom:0}
.hero .kicker{position:absolute;left:183px;top:104px;font-size:20px;line-height:26px;color:#fff}
.hero .kicker b{font-weight:700}
.hero h1{position:absolute;left:180px;top:128px;font-weight:300;font-size:62px;line-height:72px;color:#fff}
.hero .sale-line{position:absolute;left:183px;top:202px;font-size:32px;line-height:40px;color:#fff}
.hero .cta{position:absolute;left:183px;top:272px;width:129px;height:36px;background:var(--yellow);color:#fff;font-size:12px;font-weight:600;text-align:center;line-height:36px}
.arrow{position:absolute;top:196px;width:28px;height:28px;border-radius:50%;background:rgba(255,255,255,.8)}
.arrow svg{position:absolute;left:9px;top:8px}

/* promos */
.ph{position:absolute}
.pink-box{left:352px;top:640px;width:262px;height:250px;background:var(--pink);color:#fff;text-align:center}
.teal-box{left:87px;top:890px;width:265px;height:250px;background:var(--teal);color:#fff;text-align:center}
.label{font-size:12px;letter-spacing:3px;text-transform:uppercase}
.promo-title{font-family:'Roboto Slab',serif;font-size:24px;line-height:30px}
.btn-outline{display:inline-block;border:1px solid #fff;font-size:11px;font-weight:600;padding:8px 26px}
.corner{position:absolute;width:50px;height:50px}
.offer{left:614px;top:640px;width:499px;height:500px;background:linear-gradient(135deg,#6e5e49,#a9814f 45%,#4f6870)}
.offer .dash{position:absolute;left:40px;top:40px;width:420px;height:420px;border:2px dashed rgba(255,255,255,.7)}
.offer .txt{position:absolute;left:0;width:499px;text-align:center;color:#fff}

/* categories */
.cats{left:0;top:1195px;width:1200px;height:563px;background:var(--light)}
.section-title{font-family:'Roboto Slab',serif;font-size:28px;line-height:36px;font-weight:300;color:#444;white-space:nowrap}
.section-title b{font-weight:700}
.section-title::after{content:"";display:inline-block;width:90px;height:2px;background:var(--teal);margin-left:16px;vertical-align:middle}
.feature-cat{left:87px;top:1306px;width:295px;height:398px;border:2px solid var(--teal);background:#fff}
.feature-cat .name{position:absolute;top:16px;width:100%;text-align:center;font-family:'Roboto Slab',serif;font-size:16px;color:#444}
.tile{position:absolute;width:211px;height:185px}
.tile .tag{position:absolute;left:0;bottom:18px;height:30px;line-height:30px;padding:0 6px;font-family:'Roboto Slab',serif;font-size:17px;color:#fff;width:180px;white-space:nowrap}
.tag.teal{background:var(--teal)}.tag.yellow{background:var(--yellow)}

/* banners */
.wide{position:absolute;top:1814px;width:487px;height:324px}
.wide .strip{position:absolute;left:0;bottom:0;width:310px;height:60px;padding:8px 14px;color:#fff}
.wide .strip b{display:block;font-family:'Roboto Slab',serif;font-weight:400;font-size:18px;line-height:24px}
.wide .strip span{font-size:12px;white-space:nowrap}

/* products */
.card{position:absolute;top:2250px;width:237px;height:347px;background:#fff;border:1px solid #eee}
.card.raised{box-shadow:0 4px 14px rgba(0,0,0,.12)}
.card .pic{position:absolute;left:14px;top:14px;width:207px;height:173px;background:#eee}
.card .new{position:absolute;left:0;top:0;width:0;height:0;border-top:34px solid var(--yellow);border-right:34px solid transparent}
.card .pname{position:absolute;left:14px;top:205px;width:210px;font-size:13px;line-height:17px;color:#444}
.card .price{position:absolute;left:14px;top:245px;font-size:17px;color:var(--teal)}
.card .price s{font-size:13px;color:#999;margin-right:4px}
.card .buy{position:absolute;left:14px;top:293px;width:130px;height:34px;background:var(--teal);color:#fff;font-size:12px;font-weight:600;text-align:center;line-height:34px}
.card .buy.yellow{background:var(--yellow)}
.card .view{position:absolute;left:152px;top:293px;width:34px;height:34px;background:var(--teal)}

/* shipping */
.ship-title{left:0;top:2680px;width:1200px;text-align:center;font-family:'Roboto Slab',serif;font-size:40px;line-height:50px;color:var(--teal)}
.ship-title span{color:var(--yellow)}
.ship-sub{left:0;top:2734px;width:1200px;text-align:center;font-size:21px;letter-spacing:1px;color:#444}
.ship-btn{left:517px;top:2790px;width:166px;height:38px;background:var(--teal);color:#fff;font-size:12px;font-weight:600;text-align:center;line-height:38px}
.perks{left:59px;top:2869px;width:1082px;height:213px;background:#fafafa;display:flex}
.perk{flex:1;text-align:center;padding-top:30px;border-right:1px solid #e8e8e8}
.perk:last-child{border:0}
.perk h4{font-size:14px;font-weight:600;letter-spacing:1px;margin-top:14px;color:#444}
.perk p{font-size:12px;line-height:20px;color:#888;margin:12px auto 0;width:250px}

/* footer */
.footer{left:0;top:3082px;width:1200px;height:434px;background:var(--teal);color:#fff}
.footer .brand{position:absolute;left:87px;top:40px;font-family:'Roboto Slab',serif;font-weight:700;font-size:44px;line-height:54px}
.footer .about{position:absolute;left:87px;top:120px;width:300px;font-size:14px;line-height:21px}
.footer .about-btn{position:absolute;left:87px;top:225px;width:129px;height:36px;border:1px solid var(--yellow);font-size:12px;text-align:center;line-height:34px}
.footer h5{position:absolute;top:50px;font-size:17px;font-weight:600}
.footer .contact{position:absolute;left:438px;top:104px;font-size:13px;line-height:21px}
.footer .contact .phone{font-size:16px;font-weight:700;margin-top:6px}
.footer .contact u{text-decoration:underline}
.social{position:absolute;top:236px;width:30px;height:30px;border:1px solid #fff;border-radius:50%}
.social.on{background:#fff}
.footer .news{position:absolute;left:813px;top:104px;width:300px;font-size:13px;line-height:20px}
.footer .input{position:absolute;left:813px;top:171px;width:298px;height:34px;background:rgba(255,255,255,.3);font-size:12px;padding:9px 12px}
.footer .send{position:absolute;left:813px;top:225px;width:132px;height:36px;background:var(--yellow);font-size:13px;font-weight:600;text-align:center;line-height:36px}
.footer .rule{position:absolute;left:87px;top:301px;width:1026px;height:1px;background:rgba(255,255,255,.5)}
.footer .fnav{position:absolute;left:112px;top:313px;width:990px;display:flex;justify-content:space-between;font-size:14px}
.footer .fnav .cur{text-decoration:underline}
.footer .copy{position:absolute;left:87px;top:383px;font-size:12px}
.footer .top-btn{position:absolute;left:1086px;top:380px;width:26px;height:26px;border-radius:50%;background:var(--yellow)}
</style>
</head>
<body>

<div class="abs topbar">
  <div class="links"><span>About Us</span>| <span class="active">Customer Service</span>| <span>Help &amp; FAQ</span>| <span>Return Policy</span>| <span>Shipping Information</span>| <span>Contact Us</span></div>
  <div class="login">&#9679; Login</div>
  <div class="cart">Cart</div>
</div>

<div class="abs logo">Novabrite</div>
<div class="abs search">Search...
  <div class="btn"><svg width="15" height="15" viewBox="0 0 15 15"><circle cx="6" cy="6" r="4.5" fill="none" stroke="#fff" stroke-width="2"/><path d="M9.5 9.5l4 4" stroke="#fff" stroke-width="2"/></svg></div>
</div>
<div class="abs call"><b>Call Us:</b> &#9742; 555 - 204 - 3188</div>

<nav class="abs nav"><ul>
  <li class="home">Home</li><li>Party Supplies</li><li>Occasions &amp; Events</li><li>Toys &amp; Games</li><li>Crafts</li><li>Teacher Supplies</li><li>Wedding</li><li>Holidays</li><li class="sale">Sale</li>
</ul></nav>

<section class="abs hero" role="img" aria-label="Woman in a sun hat and swimsuit sitting on a sandy beach by the sea">
  <div class="frame"></div>
  <div class="kicker">Summer Fun with <b>Super Savings!</b></div>
  <h1>Summer Wear</h1>
  <div class="sale-line">Sale Uo to <b>50% off</b></div>
  <div class="cta">Shop Now</div>
  <div class="arrow" style="left:20px"><svg width="10" height="12"><path d="M8 1L2 6l6 5" fill="none" stroke="#666" stroke-width="2"/></svg></div>
  <div class="arrow" style="left:1152px"><svg width="10" height="12"><path d="M2 1l6 5-6 5" fill="none" stroke="#666" stroke-width="2"/></svg></div>
</section>

<div class="ph" style="left:87px;top:640px;width:265px;height:250px;background:linear-gradient(135deg,#8fc9a8,#f2c66b 50%,#6ab6d8)" role="img" aria-label="Colourful bunting and wrapped gift boxes"></div>
<div class="ph pink-box">
  <svg class="corner" style="left:18px;top:18px"><path d="M2 50V2h48" fill="none" stroke="#fff" stroke-width="2"/></svg>
  <div class="label" style="margin-top:42px">Party Supplies</div>
  <div class="promo-title" style="margin-top:20px">Sports Party<br>Supplies</div>
  <div class="btn-outline" style="margin-top:22px">Shop Now</div>
</div>
<div class="ph teal-box">
  <svg class="corner" style="left:18px;top:182px"><path d="M2 0v48h48" fill="none" stroke="#fff" stroke-width="2"/></svg>
  <div class="label" style="margin-top:70px">Toys &amp; Games</div>
  <div class="promo-title" style="margin-top:20px">Fidget Spinners &amp;<br>Fidget Toys</div>
</div>
<div class="ph" style="left:352px;top:890px;width:262px;height:250px;background:linear-gradient(160deg,#e8ecef,#f4d24a 55%,#e79a3a)" role="img" aria-label="Child playing with a pile of rubber ducks"></div>
<div class="ph offer" role="img" aria-label="Hand holding a colourful light-up mug">
  <div class="dash"></div>
  <div class="txt label" style="top:158px;font-size:11px">Best Offer</div>
  <div class="txt" style="top:180px;font-family:'Roboto Slab',serif;font-size:44px;line-height:54px">Up to <b>70% Off</b></div>
  <div class="txt" style="top:240px;font-family:'Roboto Slab',serif;font-size:22px">Clearance Sale</div>
  <div class="txt" style="top:300px"><span class="btn-outline">Shop Now</span></div>
</div>

<section class="abs cats">
  <h2 class="section-title" style="position:absolute;left:87px;top:48px">Shop <b>Categories</b></h2>
</section>
<div class="abs feature-cat">
  <div class="name">---- Novelty Sunglasses ----</div>
  <div style="position:absolute;left:40px;top:60px;width:211px;height:320px;background:linear-gradient(180deg,#f7f7f7,#f4b4c6)" role="img" aria-label="Girl wearing pink novelty sunglasses"></div>
</div>
<div class="tile" style="left:422px;top:1308px;background:linear-gradient(135deg,#f6b8cf,#e5e0f0)" role="img" aria-label="Candy buffet jars"><div class="tag teal">Candy Buffet</div></div>
<div class="tile" style="left:663px;top:1308px;background:linear-gradient(135deg,#eee,#b9543f 60%,#d8c9b4)" role="img" aria-label="Handbags"><div class="tag yellow">Bags</div></div>
<div class="tile" style="left:905px;top:1308px;background:linear-gradient(135deg,#6fb8e0,#e04a3a 55%,#f2c94c)" role="img" aria-label="Carnival games"><div class="tag teal">Carnival</div></div>
<div class="tile" style="left:422px;top:1519px;background:linear-gradient(135deg,#f3efe6,#9ec7e6 50%,#f0a84a)" role="img" aria-label="Assorted toys on shelves"><div class="tag teal">Assortments</div></div>
<div class="tile" style="left:663px;top:1519px;background:linear-gradient(135deg,#7d5fb0,#f3a2c1 55%,#5ab0d8)" role="img" aria-label="Birthday party decorations"><div class="tag teal">Birthday Party</div></div>
<div class="tile" style="left:905px;top:1519px;background:linear-gradient(135deg,#e8edf0,#6fa7c9 50%,#e6b35a)" role="img" aria-label="Pencils and craft materials"><div class="tag teal">Craft Supplies</div></div>

<div class="wide" style="left:98px;background:linear-gradient(135deg,#e9e6e0,#d7533e 45%,#5aa36b 70%,#f2c64d)" role="img" aria-label="Lanyards and colourful stacked paper trays">
  <div class="strip" style="background:var(--teal)"><b>Back to School</b><span>400+ New Items for Back to School</span></div>
</div>
<div class="wide" style="left:626px;background:linear-gradient(135deg,#a9cfd9,#6aa7c9 40%,#f0c24a 70%,#e7e3d9)" role="img" aria-label="Craft kits and an inflatable beach ball">
  <div class="strip" style="background:var(--yellow)"><b>Summer Crafts</b><span>100s of Fun Summer Crafts for All Ages</span></div>
</div>

<h2 class="abs section-title" style="left:87px;top:2184px">Featured <b>Products</b></h2>

<div class="card" style="left:87px"><div class="pic" role="img" aria-label="Neon animal print hats"></div><div class="new"></div>
  <div class="pname">Neon Animal Print Gangster Hats Assortment</div>
  <div class="price"><s>$ 9.99</s> $7.98</div><div class="buy">Shop Now</div></div>
<div class="card raised" style="left:349px"><div class="pic" role="img" aria-label="Colorful tote bags"></div><div class="new"></div>
  <div class="pname">Personalized Large Bright Color Tote Bags</div>
  <div class="price"><s>$ 45.99</s> $39.98</div><div class="buy yellow">Shop Now</div>
  <div class="view"><svg width="34" height="34"><ellipse cx="17" cy="17" rx="8" ry="5" fill="none" stroke="#fff" stroke-width="1.5"/><circle cx="17" cy="17" r="2" fill="#fff"/></svg></div></div>
<div class="card" style="left:612px"><div class="pic" role="img" aria-label="Mini beach playsets"></div>
  <div class="pname">Colorful Mini Beach Playsets</div>
  <div class="price">$11.99</div><div class="buy">Shop Now</div></div>
<div class="card" style="left:874px"><div class="pic" role="img" aria-label="Inflatable flamingo coasters"></div><div class="new"></div>
  <div class="pname">Inflatable Floating Flamingo Coasters</div>
  <div class="price"><s>$ 9.49</s> $7.98</div><div class="buy">Shop Now</div></div>

<svg class="abs" style="left:0;top:2597px" width="1200" height="485">
  <polygon points="0,0 560,485 0,485" fill="#eaae3c"/>
  <polygon points="1200,0 640,485 1200,485" fill="#5ea7b1"/>
</svg>
<div class="abs ship-title">Free shipping <span>on orders over $99</span></div>
<div class="abs ship-sub">this offer is valid on all our store items</div>
<div class="abs ship-btn">Shop Now Products</div>

<div class="abs perks">
  <div class="perk"><svg width="40" height="40" viewBox="0 0 40 40"><path d="M6 18h7v18H6zM15 18l7-14c3 0 4 2 4 5l-1 7h9c2 0 3 2 3 4l-3 12c-1 2-2 3-4 3H15z" fill="var(--teal)"/></svg>
    <h4>100% GUARANTEE</h4><p>Lorem Ipsum has been the industry's standard dummy text ever</p></div>
  <div class="perk"><svg width="40" height="40" viewBox="0 0 40 40"><rect x="6" y="12" width="28" height="22" fill="var(--teal)"/><rect x="4" y="6" width="32" height="8" fill="var(--teal-dark)"/></svg>
    <h4>FREE SHIPPING &amp; RETURN</h4><p>Lorem Ipsum has been the industry's standard dummy text ever</p></div>
  <div class="perk"><svg width="40" height="40" viewBox="0 0 40 40"><path d="M6 24v-4a14 14 0 0 1 28 0v4" fill="none" stroke="var(--teal)" stroke-width="3"/><rect x="4" y="22" width="8" height="12" rx="2" fill="var(--teal)"/><rect x="28" y="22" width="8" height="12" rx="2" fill="var(--teal)"/></svg>
    <h4>24/7 SUPPORT</h4><p>Lorem Ipsum has been the industry's standard dummy text ever</p></div>
</div>

<footer class="abs footer">
  <div class="brand">Novabrite</div>
  <p class="about">There are many variations of passages of Lorem Ipsum available, but the majority have suffered alteration in some form, by injected humour, or randomise...</p>
  <div class="about-btn">About Us</div>
  <h5 style="left:438px">Contact Us</h5>
  <div class="contact">4410 Orchard Lane, Brookvale,<br>OR 97201
    <div class="phone">Call Us: &nbsp;555 - 204 - 3188</div>
    <u>info@novabrite.com</u></div>
  <div class="social" style="left:438px"></div>
  <div class="social on" style="left:478px"></div>
  <div class="social" style="left:518px"></div>
  <h5 style="left:813px">Sign Up Newsletter</h5>
  <p class="news">You Want to get Update about anything New? Join our newsletter</p>
  <div class="input">Enter Your Email...</div>
  <div class="send">&#10148; Send</div>
  <div class="rule"></div>
  <div class="fnav"><span class="cur">Home</span><span>Party Supplies</span><span>Occasions &amp; Events</span><span>Toys &amp; Games</span><span>Crafts</span><span>Teacher Supplies</span><span>Wedding</span><span>Holidays</span><span>Sale</span></div>
  <div class="copy">© 2017 Novabrite. All Rights Reserved. &nbsp; Terms of use &nbsp;/ &nbsp;Privacy Policy</div>
  <div class="top-btn"><svg width="26" height="26"><path d="M9 15l4-4 4 4" fill="none" stroke="#fff" stroke-width="2"/></svg></div>
</footer>

</body>
</html>
```